Services Brochure

We need an revised brochure for our 3 main services. I have uploaded our old Brochure for reference. We have 3 main services (Managed IT Services, Business VoIP, Business Internet). Below is some text we would like included in the brochure for each service section. In addition I have attached a "mock up" showing that we want IT Services on top, VoIP in the middle and Internet at the bottom. Please use your design experience to select images that would fit well. I also included an image of the phone we would like to use.
Text for Brochure:
Title/Header: Unleash the Power of Local IT Solutions
IT Services That Mean Business
Experience fanatical customer service with our affordable, full-service IT solutions. We’re 100% local, ensuring leading response times and personalized support—so you can focus on what you do best.
Talk More, Worry Less with Our Telephone Services
Say goodbye to overpriced equipment and hello to our free phone plan. Keep your number and enjoy unlimited local and long-distance calling. Tailor your phone system to your business needs and rest assured—our rates are always the lowest in town.
Highspeed Internet That Sets You Apart
Stay connected with blazing-fast speeds—from 1Gbps to 10Gbps, both up and down. Benefit from a static IP address and unbeatable prices, backed by 100% local support. Get the connectivity your business deserves at the best value in town.
Elevate your business with cutting-edge technology.
Sorry everyone the banner size is 81" high and 33" wide.

```html
<!DOCTYPE html>
<html lang="en">
<head>
<meta charset="utf-8">
<title>Nexora – Local IT Solutions Banner</title>
<link href="https://fonts.googleapis.com/css2?family=Orbitron:wght@800;900&family=Outfit:wght@300;400;600&family=Poppins:wght@800&display=swap" rel="stylesheet">
<style>
  :root{
    --navy:#2b2e7f;
    --navy-dark:#1d1f5c;
    --steel:#8c8d90;
    --panel:#e1e2e4;
    --paper:#f7f7f8;
    --ink:#2f2f33;
    --backdrop:#6b6b6b;
    --white:#ffffff;
  }
  *{margin:0;padding:0;box-sizing:border-box}
  html,body{width:1200px;height:2432px;overflow:hidden;background:var(--backdrop)}
  .banner{position:absolute;left:166px;top:123px;width:905px;height:2218px;
    background:linear-gradient(180deg,#fafafa 0%,var(--paper) 40%,#f3f3f5 100%);overflow:hidden}
  .brand{position:absolute;top:40px;left:0;width:100%;text-align:center;
    font-family:"Outfit",sans-serif;font-weight:600;font-size:150px;line-height:1;color:var(--navy);letter-spacing:-2px}
  .headline-band{position:absolute;top:254px;left:0;width:100%;height:164px;background:var(--navy);text-align:center}
  .headline-band .line-one{position:absolute;top:26px;width:100%;font-family:"Orbitron",sans-serif;font-weight:900;font-size:44px;color:var(--white);letter-spacing:1px}
  .headline-band .line-two{position:absolute;top:78px;width:100%;font-family:"Orbitron",sans-serif;font-weight:900;font-size:56px;color:#a7a8ab;letter-spacing:1px;text-shadow:2px 3px 3px rgba(0,0,0,.35)}
  .service-panel{position:absolute;background:var(--panel)}
  .panel-right{left:225px;width:601px;height:449px;clip-path:polygon(0 0,100% 0,100% 79%,81% 100%,0 100%)}
  .panel-left{left:65px;width:601px;height:448px;clip-path:polygon(0 0,100% 0,100% 100%,18% 100%,0 79%)}
  .service-photo{position:absolute;width:357px;height:312px}
  .service-title{position:absolute;font-family:"Poppins",sans-serif;font-weight:800;font-size:35px;line-height:37px;color:var(--navy)}
  .service-copy{position:absolute;font-family:"Outfit",sans-serif;font-weight:300;font-size:25px;line-height:31.8px;color:var(--ink)}
  .tagline{position:absolute;top:1888px;left:0;width:100%;text-align:center;font-family:"Poppins",sans-serif;font-weight:800;color:var(--navy)}
  .tagline .lead{display:block;font-size:41px;line-height:54px}
  .tagline .emphasis{display:block;font-size:46px;line-height:54px}
  .contact-band{position:absolute;top:2056px;left:0;width:100%;height:162px;background:var(--navy)}
  .phone-tab{position:absolute;top:2042px;left:0;width:905px;height:92px}
  .phone-number{position:absolute;top:2058px;left:0;width:100%;text-align:center;font-family:"Poppins",sans-serif;font-weight:800;font-size:50px;line-height:60px;color:var(--white);letter-spacing:1px}
  .phone-number svg{vertical-align:-6px;margin-right:12px}
  .contact-line{position:absolute;top:2148px;left:0;width:100%;text-align:center;font-family:"Poppins",sans-serif;font-weight:800;font-size:34px;line-height:50px;color:var(--white)}
  .contact-line svg{vertical-align:-7px;margin-right:10px}
  .contact-line .gap{display:inline-block;width:30px}
</style>
</head>
<body>
<main class="banner">
  <div class="brand">nexora</div>

  <header class="headline-band">
    <div class="line-one">UNLEASH THE POWER OF</div>
    <div class="line-two">LOCAL IT SOLUTIONS</div>
  </header>

  <!-- Managed IT -->
  <section>
    <div class="service-panel panel-right" style="top:455px"></div>
    <svg class="service-photo" style="left:59px;top:521px" viewBox="0 0 380 330" role="img" aria-label="Photo of a support technician with headset at a monitor in a server room">
      <defs><linearGradient id="gradServer" x1="0" y1="0" x2="1" y2="1"><stop offset="0" stop-color="#0f2a3a"/><stop offset=".6" stop-color="#16252f"/><stop offset="1" stop-color="#c9c9cc"/></linearGradient></defs>
      <polygon points="2,165 96,2 284,2 378,165 284,328 96,328" fill="#fff" stroke="var(--navy)" stroke-width="3"/>
      <polygon points="20,165 106,16 274,16 360,165 274,314 106,314" fill="url(#gradServer)"/>
    </svg>
    <h2 class="service-title" style="left:438px;top:500px">MANAGED<br>IT SERVICES</h2>
    <p class="service-copy" style="left:438px;top:586px">Experience fanatical<br>customer service with our<br>affordable, full-service IT<br>solutions. We’re 100% local,<br>ensuring leading response<br>times and personalized<br>support—so you can focus on<br>what you do best.</p>
  </section>

  <!-- VoIP -->
  <section>
    <div class="service-panel panel-left" style="top:930px"></div>
    <svg class="service-photo" style="left:473px;top:995px" viewBox="0 0 380 330" role="img" aria-label="Photo of a hand lifting the receiver of a desk phone">
      <defs><linearGradient id="gradPhone" x1="0" y1="0" x2="1" y2="1"><stop offset="0" stop-color="#3a3b3e"/><stop offset=".5" stop-color="#9a9b9e"/><stop offset="1" stop-color="#c9a57a"/></linearGradient></defs>
      <polygon points="2,165 96,2 284,2 378,165 284,328 96,328" fill="#fff" stroke="var(--navy)" stroke-width="3"/>
      <polygon points="20,165 106,16 274,16 360,165 274,314 106,314" fill="url(#gradPhone)"/>
    </svg>
    <h2 class="service-title" style="left:123px;top:972px">BUSINESS VOIP</h2>
    <p class="service-copy" style="left:123px;top:1011px">Say goodbye to overpriced<br>equipment and hello to our free<br>phone plan. Keep your number<br>and enjoy unlimited local and<br>long-distance calling. Tailor<br>your phone system to your<br>business needs and rest<br>assured—our rates are always<br>the lowest in town.</p>
  </section>

  <!-- Internet -->
  <section>
    <div class="service-panel panel-right" style="top:1403px"></div>
    <svg class="service-photo" style="left:59px;top:1469px" viewBox="0 0 380 330" role="img" aria-label="Abstract image of glowing fibre-optic light streaks">
      <defs><radialGradient id="gradFibre" cx=".22" cy=".45" r=".9"><stop offset="0" stop-color="#f4d8f0"/><stop offset=".25" stop-color="#a04fb0"/><stop offset=".6" stop-color="#3a3fb0"/><stop offset="1" stop-color="#0c0c3a"/></radialGradient></defs>
      <polygon points="2,165 96,2 284,2 378,165 284,328 96,328" fill="#fff" stroke="var(--navy)" stroke-width="3"/>
      <polygon points="20,165 106,16 274,16 360,165 274,314 106,314" fill="url(#gradFibre)"/>
    </svg>
    <h2 class="service-title" style="left:438px;top:1442px">BUSINESS<br>INTERNET</h2>
    <p class="service-copy" style="left:438px;top:1525px">Stay connected with<br>blazing-fast speeds—from<br>1Gbps to 10Gbps, both up and<br>down. Benefit from a static IP<br>address and unbeatable prices,<br>backed by 100% local support.<br>Get the connectivity your<br>business deserves at the best<br>value in town.</p>
  </section>

  <p class="tagline"><span class="lead">Elevate your business with</span><span class="emphasis">CUTTING-EDGE TECHNOLOGY</span></p>

  <footer>
    <div class="contact-band"></div>
    <svg class="phone-tab" viewBox="0 0 905 92" aria-hidden="true"><polygon points="155,0 754,0 695,91 211,91" fill="var(--navy-dark)"/></svg>
    <div class="phone-number"><svg width="36" height="44" viewBox="0 0 24 28" aria-hidden="true"><path d="M7 2 L10 8 L7.5 10 C8.5 14 10.5 18 14 21 L16.5 19 L21 24 L17.5 27 C9 24 3 13 3.5 4 Z" fill="none" stroke="#fff" stroke-width="2.2" stroke-linejoin="round"/></svg>555-014-2387</div>
    <div class="contact-line"><svg width="40" height="30" viewBox="0 0 40 30" aria-hidden="true"><rect x="1.5" y="1.5" width="37" height="27" fill="none" stroke="#fff" stroke-width="2.5"/><path d="M1.5 1.5 L20 17 L38.5 1.5 M1.5 28.5 L15 13 M38.5 28.5 L25 13" fill="none" stroke="#fff" stroke-width="2.5"/></svg>sales@nexoranet.com<span class="gap"></span><svg width="36" height="36" viewBox="0 0 36 36" aria-hidden="true"><g fill="none" stroke="#fff" stroke-width="2.2"><circle cx="18" cy="18" r="16"/><ellipse cx="18" cy="18" rx="7" ry="16"/><path d="M2 18 H34 M5 10 H31 M5 26 H31 M18 2 V34"/></g></svg>www.nexoranet.com</div>
  </footer>
</main>
</body>
</html>
```